To revamp a new website www.veltromiflow.com

We would need to revamp a new website that is corporate looking, professional and clean look.
We would need CMS features, no e-commerce and no member access.
For a start, please refer to the current website for the wordings and photos

The changes from the current website beside the overall design, outline and feel are that we will take out 3 products and put in 1 new product.

We will provide the information for the products that are to be deleted and the new additional ones as we go along

Corporate

It Professional

Font styles to use
Sans Serif

Colors
5c5c5c
ffffff
fbed22

Requirements
Must have
• CMS system for easy updating
• Workable on tablet, phone, laptop and desktop
• Professional, corporate look
• Upmarket feeling
• Clean, Distinctive and stand out design
• Flash on the first page
• Corporate color of grey and yellow with white background for the corporate look
Nice to have
• Nice photos for the contact us and news section
Should not have
• No registration
• No e commerce
• no multiple language

```html
<!DOCTYPE html>
<html lang="en">
<head>
<meta charset="utf-8">
<title>Veltromi Flow</title>
<link rel="stylesheet" href="https://fonts.googleapis.com/css2?family=Lato:ital,wght@0,400;0,700;1,400&family=Raleway:wght@300;400;500&family=Ubuntu:wght@500;700&display=swap">
<style>
:root{
  --yellow:#fbed22;
  --navy:#03026b;
  --grey:#5c5c5c;
  --grey-light:#8a8a8a;
  --panel:#f2f2f2;
  --white:#ffffff;
  --line:#c9c9e6;
}
*{box-sizing:border-box;margin:0;padding:0}
html,body{width:1200px;height:2835px;overflow:hidden}
body{font-family:"Lato",sans-serif;color:var(--grey);background:var(--white);position:relative}
a{color:inherit;text-decoration:none}

.topbar{height:40px;background:var(--yellow);display:flex;align-items:center;padding:0 80px;font-size:13px;font-weight:700;color:#222}
.topbar .greeting{width:440px}
.topbar .social{display:flex;gap:22px;width:270px}
.topbar .social span{width:11px;height:11px;border-radius:50%;background:#555}
.topbar .contact{display:flex;gap:30px;margin-left:auto}
.topbar .contact span{display:flex;align-items:center;gap:8px}

.hero{position:relative;height:555px;overflow:hidden}
.hero .photo{position:absolute;inset:0;background:radial-gradient(ellipse 420px 300px at 600px 470px,#3a3d40 0%,#8c9196 45%,#d4d8da 62%,transparent 64%),linear-gradient(180deg,#f4f7f7 0%,#cfe6e5 40%,#8fc8c6 70%,#e8f2f2 100%)}
.hero h1{position:relative;font-family:"Ubuntu",sans-serif;font-weight:700;font-size:52px;line-height:74px;text-align:center;color:#555;padding-top:38px}

.mainnav{height:82px;background:var(--navy);position:relative;display:flex;align-items:center;font-family:"Raleway",sans-serif;font-size:17px;color:var(--white)}
.mainnav ul{list-style:none;display:flex;position:absolute}
.mainnav .left{left:175px;gap:48px}
.mainnav .right{left:737px;gap:48px}
.mainnav .active{color:var(--yellow)}
.brandmark{position:absolute;left:550px;top:-30px;width:100px;text-align:center}
.brandmark .disc{width:84px;height:84px;margin:0 auto;border-radius:50%;background:var(--navy);border:5px solid var(--white)}
.brandmark .name{font-family:"Lato",sans-serif;font-weight:700;font-size:17px;color:var(--white);margin-top:2px}

.welcome{height:345px;text-align:center;padding-top:50px}
.welcome .lead{font-family:"Raleway",sans-serif;font-weight:300;font-size:52px;line-height:56px;color:#555}
.welcome .company{font-family:"Raleway",sans-serif;font-weight:400;font-size:50px;line-height:62px;color:var(--navy)}
.welcome .region{display:inline-block;font-family:"Raleway",sans-serif;font-weight:500;font-size:32px;line-height:44px;color:#555;border-bottom:2px solid var(--navy);padding:0 4px 4px}
.welcome p{width:760px;margin:22px auto 0;font-size:15px;line-height:25px}

.features{height:521px;background:var(--panel);display:flex;gap:23px;padding:50px 0 0 78px}
.feature{width:333px}
.feature h2{font-family:"Raleway",sans-serif;font-weight:400;font-size:28px;text-align:center;color:#333;height:52px}
.feature .photo{height:208px}
.feature p{font-size:13px;line-height:23px;padding:16px 4px 0;height:108px}
.feature .more{font-size:13px;font-weight:700;color:#222;padding:0 4px;height:28px}
.feature .rule{border-bottom:1px solid #d8d8c0;margin-top:4px}
.photo-a{background:radial-gradient(circle at 50% 60%,#2c3aa6 0%,#1b2470 30%,#8a929c 55%,#c9cfd4 80%)}
.photo-b{background:linear-gradient(180deg,#4d86c9 0%,#8fb6de 40%,#c9a04a 65%,#6c6a5e 100%)}
.photo-c{background:linear-gradient(135deg,#d8d2c8 0%,#e37c38 40%,#2e5fb0 75%,#f0c419 100%)}

.products{height:417px;display:flex;padding-top:52px}
.product{flex:1;text-align:center;border-right:1px solid #ddd;height:312px}
.product:last-child{border-right:none}
.product .photo{width:60px;height:210px;margin:0 auto;border-radius:6px;background:linear-gradient(90deg,#6f7378,#e9ecee 45%,#9ba0a5 70%,#4c5055)}
.product h3{font-family:"Raleway",sans-serif;font-weight:400;font-size:22px;color:#333;margin-top:28px}
.product small{display:block;font-size:13px;margin-top:6px}

.testimonial{height:365px;position:relative;text-align:center;color:var(--white)}
.testimonial .photo{position:absolute;inset:0;background:linear-gradient(180deg,#3a3a3a 0%,#5b5a56 45%,#2f2f2f 100%)}
.testimonial .inner{position:relative;padding-top:60px}
.avatar{width:84px;height:84px;margin:0 auto;border-radius:50%;border:3px solid var(--yellow);background:#c9b89a;position:relative}
.avatar .quote{position:absolute;left:25px;bottom:-22px;width:30px;height:30px;border-radius:50%;background:var(--white);display:flex;align-items:center;justify-content:center}
.testimonial p{width:780px;margin:30px auto 0;font-style:italic;font-size:13px;line-height:24px}
.testimonial .author{font-family:"Raleway",sans-serif;font-size:19px;color:var(--yellow);margin-top:18px}

.inquiry{height:385px;position:relative}
.inquiry h2{font-family:"Raleway",sans-serif;font-weight:300;font-size:40px;color:#555;text-align:center;padding-top:48px}
.field{position:absolute;border:2px solid #dcdcef;background:var(--white);font-size:13px;color:#999;padding:10px 16px;font-family:Arial,sans-serif}
.send{position:absolute;left:1000px;top:291px;width:105px;height:41px;background:var(--yellow);color:#333;font-size:20px;display:flex;align-items:center;justify-content:center;font-family:Arial,sans-serif}

.footer{height:125px;background:var(--navy);position:relative;color:var(--white)}
.footer .disc{position:absolute;left:556px;top:-26px;width:88px;height:88px;border-radius:50%;background:var(--navy);border:5px solid var(--white)}
.footer ul{list-style:none;display:flex;gap:28px;position:absolute;left:80px;top:30px;font-size:13px}
.footer .social{position:absolute;right:80px;top:16px;display:flex;gap:12px}
.footer .social span{width:40px;height:40px;border-radius:50%;background:var(--white)}
.footer .copy{position:absolute;left:0;right:0;top:90px;border-top:1px solid #24238a;margin:0 80px;padding-top:8px;text-align:center;font-size:13px;font-weight:700}
.footer .copy b{color:var(--yellow)}
</style>
</head>
<body>

<header class="topbar">
  <div class="greeting">Hello Guest! Welcome to VELTROMI</div>
  <div class="social"><span></span><span></span><span></span><span></span></div>
  <div class="contact">
    <span><svg width="14" height="14" viewBox="0 0 24 24"><path fill="#222" d="M6.6 10.8a15 15 0 0 0 6.6 6.6l2.2-2.2c.3-.3.7-.4 1-.2 1.1.4 2.3.6 3.6.6.6 0 1 .4 1 1V20c0 .6-.4 1-1 1A17 17 0 0 1 3 4c0-.6.4-1 1-1h3.5c.6 0 1 .4 1 1 0 1.3.2 2.5.6 3.6.1.3 0 .7-.2 1z"/></svg>(613) 9400 2718</span>
    <span><svg width="16" height="12" viewBox="0 0 16 12"><rect x="0.5" y="0.5" width="15" height="11" fill="#222"/><path d="M1 1l7 5 7-5" stroke="#fbed22" fill="none"/></svg>sales@veltromiflow.com</span>
  </div>
</header>

<section class="hero">
  <div class="photo" role="img" aria-label="Steel pump impeller set against a breaking sea wave"></div>
  <h1>Determination, Commitment &amp; Most<br>importantly Passion to SUCCEED</h1>
</section>

<nav class="mainnav">
  <ul class="left"><li class="active">HOME</li><li>ABOUT</li><li>PRODUCT</li></ul>
  <div class="brandmark"><div class="disc"></div><div class="name">VELTROMI</div></div>
  <ul class="right"><li>NEWS</li><li>CAREERS</li><li>CONTACT</li></ul>
</nav>

<section class="welcome">
  <div class="lead">Welcome to</div>
  <div class="company">VELTROMI FLOW</div>
  <div class="region">MERIDIAN-FLOW AUSTRALIA</div>
  <p>Our Passion for Excellence is a formidable Force that will Carry us Relentlessly to meet and exceed our challenge, we believe in it, we fight for it &amp; we will Deliver.</p>
</section>

<section class="features">
  <article class="feature">
    <h2>Improved Pump Series</h2>
    <div class="photo photo-a" role="img" aria-label="Close view of a pump casing with blue impeller"></div>
    <p>Lorem Ipsum is simply dummy text of the printing and typesetting industry. Lorem Ipsum has been the industry's standard dummy text ever since the 1500s,</p>
    <div class="more"></div>
    <div class="rule"></div>
  </article>
  <article class="feature">
    <h2>Our Vision</h2>
    <div class="photo photo-b" role="img" aria-label="Yellow pipelines at an industrial plant under blue sky"></div>
    <p>To be the recognized leader in the deep well pumps and motor markets, as measured by quality, service, and growth.</p>
    <div class="more">RAED MORE</div>
    <div class="rule"></div>
  </article>
  <article class="feature">
    <h2>Our Mission</h2>
    <div class="photo photo-c" role="img" aria-label="Engineers in hard hats turning a valve on site"></div>
    <p>We are committed to providing our customers with the products that have differentiated and value added features.</p>
    <div class="more">RAED MORE</div>
    <div class="rule"></div>
  </article>
</section>

<section class="products">
  <div class="product"><div class="photo" role="img" aria-label="Stainless steel submersible pump"></div><h3>4VX PUMP</h3><small>4VX Pump</small></div>
  <div class="product"><div class="photo" role="img" aria-label="6 inch submersible pump"></div><h3>6 INCH VF PUMP</h3><small>6 Inch VF Pump</small></div>
  <div class="product"><div class="photo" role="img" aria-label="8 inch submersible pump"></div><h3>8 INCH VF PUMP</h3><small>6 Inch VF Pump</small></div>
</section>

<section class="testimonial">
  <div class="photo" role="img" aria-label="Blurred crowd walking on a city street"></div>
  <div class="inner">
    <div class="avatar" role="img" aria-label="Portrait of the client">
      <span class="quote"><svg width="14" height="10" viewBox="0 0 14 10"><path fill="#03026b" d="M0 10V5C0 2 2 0 5 0v2C3.5 2 3 3 3 4h2v6zM8 10V5c0-3 2-5 5-5v2c-1.5 0-2 1-2 2h2v6z"/></svg></span>
    </div>
    <p>Lorem Ipsum is simply dummy text of the printing and typesetting industry. Lorem Ipsum has been the industry's standard dummy text ever since the 1500s, when an unknown printer took a galley of type and scrambled it to make a type specimen book. It has survived not only five centuries, but also the leap into electronic typesetting.</p>
    <div class="author">MARLA PENROSE</div>
  </div>
</section>

<section class="inquiry">
  <h2>Quick Inquiry</h2>
  <div class="field" style="left:95px;top:133px;width:500px;height:42px">Name</div>
  <div class="field" style="left:95px;top:185px;width:500px;height:42px">Email</div>
  <div class="field" style="left:95px;top:237px;width:500px;height:42px">Subject</div>
  <div class="field" style="left:605px;top:133px;width:500px;height:146px">Message</div>
  <div class="send">Send</div>
</section>

<footer class="footer">
  <div class="disc"></div>
  <ul><li>Home</li><li>About Us</li><li>Product</li><li>News</li><li>Career</li><li>Contact Us</li></ul>
  <div class="social"><span></span><span></span><span></span><span></span></div>
  <div class="copy">© <b>VELTROMI FLOW</b> - 2016. All Rights Reserved.</div>
</footer>

</body>
</html>
```